Business Card Design

Business Card for professional consulting firm working with large financial institutions.

Target Market(s)

Executive buyers

Industry/Entity Type

Banking

Contact Information for Business Card

Mild creativity wanted. Not boring, but do elaborate artwork.

Font styles to use
Serif
Sans Serif

Colors

Designer to choose colors to be used in the design.

Requirements
Must have
• Standard business card features - company name, individual name, telephone, website, email, locations.
Nice to have
• Two colors
Should not have
• too many colors, fancy printing, cartoons.

```html
<!DOCTYPE html>
<html lang="en">
<head>
<meta charset="utf-8">
<title>k5advisory Business Card</title>
<link rel="stylesheet" href="https://fonts.googleapis.com/css2?family=Work+Sans:wght@400;500&display=swap">
<style>
  :root {
    --backdrop: #262626;
    --card: #1b1b1b;
    --card-edge: #303030;
    --silver: #dcdcdc;
    --silver-soft: #bdbdbd;
    --emboss: #4a4a4a;
    --rule: #8a8a8a;
  }
  * { box-sizing: border-box; margin: 0; padding: 0; }
  html, body {
    width: 1200px; height: 900px; overflow: hidden;
    background: var(--backdrop);
    font-family: "Work Sans", Arial, sans-serif;
  }
  .canvas {
    position: relative; width: 1200px; height: 900px;
  }
  .card {
    position: absolute; left: 280px; width: 640px; height: 366px;
    background: var(--card);
    border: 1px solid var(--card-edge);
  }
  .card-front { top: 64px; }
  .card-back { top: 470px; }
  .wordmark {
    position: absolute;
    font-weight: 500; color: var(--emboss);
    letter-spacing: 0.5px;
  }
  .card-front .wordmark {
    left: 0; right: 0; top: 150px; text-align: center; font-size: 46px;
  }
  .card-back .wordmark {
    left: 40px; top: 156px; font-size: 36px;
  }
  .divider {
    position: absolute; left: 352px; top: 60px; width: 1px; height: 246px;
    background: var(--rule);
  }
  .details {
    position: absolute; left: 384px; top: 76px; color: var(--silver);
  }
  .person-name {
    font-size: 25px; font-weight: 500; letter-spacing: 1.5px; text-transform: uppercase;
  }
  .person-role {
    font-size: 15px; color: var(--silver-soft); margin-top: 2px; letter-spacing: 0.5px;
  }
  .address {
    font-size: 15px; line-height: 22px; margin-top: 18px; letter-spacing: 0.6px;
  }
  .contact-list { list-style: none; margin-top: 10px; }
  .contact-list li {
    display: flex; align-items: center; gap: 8px;
    font-size: 16px; line-height: 24px; letter-spacing: 0.6px;
  }
  .contact-list svg { width: 11px; height: 11px; flex: none; }
</style>
</head>
<body>
<main class="canvas">
  <section class="card card-front">
    <div class="wordmark">k5advisory</div>
  </section>

  <section class="card card-back">
    <div class="wordmark">k5advisory</div>
    <div class="divider"></div>
    <div class="details">
      <h1 class="person-name">Daniel Hart</h1>
      <p class="person-role">Director</p>
      <p class="address">27 Marlow St,<br>Ashvale VIC 3610</p>
      <ul class="contact-list">
        <li>
          <svg viewBox="0 0 12 12" aria-hidden="true"><path d="M2.5 1h2l1 3-1.3 1a6 6 0 0 0 2.8 2.8L8 6.5l3 1v2c0 .8-.7 1.5-1.5 1.5A8.5 8.5 0 0 1 1 2.5C1 1.7 1.7 1 2.5 1z" fill="#dcdcdc"/></svg>
          +330 5180-4426
        </li>
        <li>
          <svg viewBox="0 0 12 12" aria-hidden="true"><rect x="1" y="2.5" width="10" height="7" fill="none" stroke="#dcdcdc" stroke-width="1.2"/><path d="M1 3l5 3.5L11 3" fill="none" stroke="#dcdcdc" stroke-width="1.2"/></svg>
          info@k5advisory.com
        </li>
        <li>
          <svg viewBox="0 0 12 12" aria-hidden="true"><circle cx="6" cy="6" r="5" fill="none" stroke="#dcdcdc" stroke-width="1.1"/><ellipse cx="6" cy="6" rx="2.2" ry="5" fill="none" stroke="#dcdcdc" stroke-width="1"/><path d="M1 6h10" stroke="#dcdcdc" stroke-width="1"/></svg>
          www.k5advisory.com
        </li>
      </ul>
    </div>
  </section>
</main>
</body>
</html>
```